Website design for an Online pastry shop

Website Name : www.lanternandplum.example

Description of the website and its target audience
We are a premium pastry company producing delicious cakes, macarons, cookies, gelato, and other sweet dessert. Our differentiation is that our products are freshly produced with premium quality imported ingredients and one bite into our products set us apart from other bakery shop. We online retail online so as to provide high quality products at a affordable cost. Our products has received raving reviews by many food enthusiast even the hard to please ones. The products contain more natural ingredients and we do not add preservatives. The return rates for our pastry is almost 80%. You only need to try once to be return customers. Our greatest challenge is getting customer to take the first bite. We are so sure of our products that we are going to give people free food tasting.

We are based in China but all our products are developed by award winning chefs from 5 stars hotel. The target customer is woman 16 to 40+ in china. Working class ladies and demand high quality products. A modern, sophisticated and minimalist website

This is a competitive market and image is crucial for such a food ‘conscious ’ orientated customer. They want to feel that they are buying from a reliable company that take great effort to ensure food cleaniness and safety yet affordable price. We make almost 98% of sub ingredients ourselves and we make it by hand.

Style/theme ideas for the web page design
I am looking for a elegant a little rustic, handmade feel yet sophisticated design - one that is easy to the eye yet functional and easy for the user to navigate through. Good play of fonts to give let it feel unique and customised. Black and white is our corporate colours. However, we do not want black background as it does not tease the taste bud. All our colours should come from our products. Customers should be very close to our products. They eat with their eyes first. Black and white is just accent.

Inspirational and competitors websites
http://www.47tart.example/ ( Key competitor )
I like the simple, clean look. The products are the key focus
https://www.pelvora.example/
clean, fresh and different. Attractive with purpose. Feminine
http://moatandwillow.example/
this has a great layout - lots of information and nicely presented. Very sweet and feminine
http://www.storeharbourly.example/
product features is the focus
http://www.janetobrill.example/store/
fun, feminine, rustic

Number of pages needed : 6 ( Uncoded PSD design only )
Page descriptions
Home Page - This page will show what makes our products stand out from the competitors and provide an introduction of who we are.
2nd page : Product catalogue
3nd page: Detail Product page with pictures and descriptions. Select products size and add to cart....
4rd page: Brand Story with pictures and descriptions.
5th page Contact Us : Here they can contact or schedule an appointment for free product tasting
6th page : Check out page

• Please see the project wire frame file " main page.png " or file number 70

```html
<!DOCTYPE html>
<html lang="en">
<head>
<meta charset="utf-8">
<title>Lantern &amp; Plum — Pastry Shop</title>
<link rel="stylesheet" href="https://fonts.googleapis.com/css2?family=Abril+Fatface&family=Lora:ital,wght@0,400;0,700;1,400&family=Source+Sans+3:ital,wght@0,300;1,300&display=swap">
<style>
  :root {
    --blush: #f5ebe6;
    --white: #ffffff;
    --ink: #111111;
    --muted: #9a8f8a;
    --soft: #c9bdb6;
    --rule: #e7dcd6;
    --lilac: #eedbf0;
    --lemon: #f6f2c4;
    --sky: #d4ecf3;
    --mint: #d9f1dc;
    --social: #d8cbc3;
  }
  * { margin: 0; padding: 0; box-sizing: border-box; }
  html, body { width: 1200px; height: 2270px; overflow: hidden; }
  body { position: relative; background: var(--blush); font-family: "Lora", Georgia, serif; color: var(--ink); }
  .abs { position: absolute; }

  .promo-bar { left: 0; top: 0; width: 1200px; height: 38px; background: var(--white);
    text-align: center; line-height: 38px; font-size: 14px; letter-spacing: 2px; font-weight: 700; }
  .promo-bar em { font-weight: 400; font-style: italic; }

  .site-header { left: 0; top: 38px; width: 1200px; height: 164px; background: var(--blush); }
  .nav-link { position: absolute; top: 114px; font-size: 14px; font-weight: 700; letter-spacing: 1px; }
  .account { position: absolute; top: 48px; left: 917px; font-size: 12px; letter-spacing: 1px; word-spacing: 4px; }
  .brand { position: absolute; left: 0; width: 1200px; top: 60px; text-align: center; }
  .brand-dot { display: block; width: 26px; height: 26px; border-radius: 50%; background: var(--ink); margin: 0 auto 14px; }
  .brand-name { font-size: 17px; letter-spacing: 1px; }

  .hero { left: 0; top: 202px; width: 1200px; height: 470px;
    background: radial-gradient(ellipse at 55% 75%, #e9a46a 0%, #d98a8a 22%, #e8cfc6 48%, #ede3de 70%),
                linear-gradient(90deg, #e6c9c9, #f2e6e2); }
  .hero-title { left: 0; width: 1200px; top: 382px; text-align: center;
    font-family: "Abril Fatface", Georgia, serif; font-size: 68px; letter-spacing: 14px; }
  .hero-rule { left: 552px; top: 493px; width: 96px; height: 3px; background: var(--ink); }

  .tagline-layer { width: 691px; height: 95px; }
  .tagline { left: 257px; top: 603px; width: 691px; height: 95px; background: var(--lilac); padding: 26px 36px; }
  .tagline h2 { font-size: 18px; font-style: italic; font-weight: 700; letter-spacing: 1.5px; }
  .tagline p { font-size: 12px; color: var(--muted); letter-spacing: 1.5px; margin-top: 6px; }

  .photo { position: absolute; box-shadow: 0 8px 18px rgba(80,50,40,.25); }
  .category-label { position: absolute; font-family: "Abril Fatface", Georgia, serif; font-size: 48px; letter-spacing: 4px; line-height: 1; }
  .category-rule { position: absolute; height: 2px; background: var(--white); }

  .newsletter-input { left: 117px; top: 1820px; width: 375px; height: 59px; background: var(--white);
    font-family: "Source Sans 3", sans-serif; font-style: italic; font-weight: 300; font-size: 14px; color: #555;
    line-height: 59px; padding-left: 30px; }
  .newsletter-button { left: 506px; top: 1820px; width: 149px; height: 59px; border: 3px solid var(--soft);
    text-align: center; line-height: 53px; font-size: 14px; color: var(--soft); letter-spacing: 1px; }
  .social-dot { position: absolute; top: 1830px; width: 42px; height: 42px; border-radius: 50%; background: var(--social); }

  .site-footer { left: 0; top: 1932px; width: 1200px; height: 338px; background: var(--white); }
  .footer-col { position: absolute; top: 76px; width: 141px; }
  .footer-col h3 { font-size: 14px; font-weight: 400; color: var(--muted); letter-spacing: 1.5px;
    padding-bottom: 10px; border-bottom: 2px solid var(--rule); }
  .footer-col li { list-style: none; font-size: 12px; color: var(--soft); letter-spacing: 1px; margin-top: 14px; line-height: 14px; }
  .footer-col ul { margin-top: 18px; }
  .copyright { position: absolute; top: 276px; left: 0; width: 1200px; text-align: center; font-size: 12px; color: var(--soft); letter-spacing: 1px; }
</style>
</head>
<body>

<div class="abs promo-bar">Free Delivery <em>for Orders above</em> $50!</div>

<header class="abs site-header">
  <span class="account">Login &nbsp;/&nbsp; Sign Up &nbsp;&nbsp;&nbsp;&nbsp; | &nbsp;&nbsp;&nbsp;&nbsp; Cart: 0</span>
  <nav>
    <span class="nav-link" style="left:111px">Cakes</span>
    <span class="nav-link" style="left:226px">Macarons</span>
    <span class="nav-link" style="left:368px">Cookies</span>
    <span class="nav-link" style="left:771px; top:112px">Gelato</span>
    <span class="nav-link" style="left:891px; top:112px">Tasting Room</span>
    <span class="nav-link" style="left:1066px; top:112px">About Us</span>
  </nav>
  <div class="brand"><span class="brand-dot"></span><span class="brand-name">Lantern &amp; Plum</span></div>
</header>

<section class="abs hero" role="img" aria-label="Close-up photo of a hand lifting a macaron above a tray of colourful gelato scoops"></section>
<h1 class="abs hero-title">PRODUCT NAME</h1>
<div class="abs hero-rule"></div>

<div class="abs tagline-layer" style="left:269px; top:619px; background:var(--lemon)"></div>
<div class="abs tagline-layer" style="left:265px; top:614px; background:var(--mint)"></div>
<div class="abs tagline-layer" style="left:261px; top:608px; background:var(--sky)"></div>
<div class="abs tagline">
  <h2>We value flavor over fuss.</h2>
  <p>Artisan, handcrafted &amp; other gourmet confections delivered direct to your door.</p>
</div>

<!-- Cakes -->
<div class="photo" style="left:146px; top:794px; width:252px; height:187px; background:linear-gradient(135deg,#3a2420,#7a4a3a)" role="img" aria-label="Photo of chocolate shavings on a cake"></div>
<div class="photo" style="left:171px; top:922px; width:282px; height:235px; background:linear-gradient(160deg,#8a1a22,#c23a40 55%,#e7c9a0)" role="img" aria-label="Photo of a cherry-topped tart"></div>
<div class="photo" style="left:334px; top:823px; width:189px; height:283px; background:radial-gradient(circle at 55% 45%,#7a1526,#b3404a 40%,#f1ddb8 65%,#efe8e2)" role="img" aria-label="Photo of a blueberry cheesecake on a plate"></div>
<span class="category-label" style="left:309px; top:1130px">CAKES</span>
<div class="category-rule" style="left:257px; top:1186px; width:271px"></div>

<!-- Macarons -->
<div class="photo" style="left:681px; top:794px; width:250px; height:187px; background:linear-gradient(180deg,#f8f6f8,#9cc6e4 55%,#eef0f3)" role="img" aria-label="Photo of a blue macaron"></div>
<div class="photo" style="left:706px; top:930px; width:282px; height:227px; background:linear-gradient(180deg,#f6f1f4,#e44f6a 50%,#f0e8ee)" role="img" aria-label="Photo of a pink macaron"></div>
<div class="photo" style="left:866px; top:823px; width:189px; height:283px; background:linear-gradient(180deg,#fbf8fb,#9a8fae 60%,#f3eff4)" role="img" aria-label="Photo of a lavender macaron"></div>
<span class="category-label" style="left:785px; top:1130px">MACARONS</span>
<div class="category-rule" style="left:790px; top:1186px; width:273px"></div>

<!-- Cookies -->
<div class="photo" style="left:146px; top:1286px; width:252px; height:187px; background:linear-gradient(135deg,#6a4a34,#c38a55)" role="img" aria-label="Photo of assorted cookies on a wooden table"></div>
<div class="photo" style="left:171px; top:1414px; width:282px; height:235px; background:linear-gradient(150deg,#8d5a38,#c48d58 50%,#6b4428)" role="img" aria-label="Photo of cookies and walnuts"></div>
<div class="photo" style="left:334px; top:1315px; width:189px; height:283px; background:radial-gradient(circle at 60% 35%,#f2c23a,#eee5dc 30%,#7a5640 70%)" role="img" aria-label="Photo of flour, egg and chocolate chips"></div>
<span class="category-label" style="left:279px; top:1622px">COOKIES</span>
<div class="category-rule" style="left:257px; top:1678px; width:271px"></div>

<!-- Gelato -->
<div class="photo" style="left:681px; top:1286px; width:250px; height:187px; background:linear-gradient(180deg,#efe0c4,#a56a5a 60%,#e0cdc4)" role="img" aria-label="Photo of gelato macaron sandwiches"></div>
<div class="photo" style="left:706px; top:1414px; width:282px; height:235px; background:linear-gradient(180deg,#f3ece2,#f1e6d6 45%,#c2434a 75%,#e6a47a)" role="img" aria-label="Photo of a gelato sandwich with berry filling"></div>
<div class="photo" style="left:866px; top:1315px; width:189px; height:283px; background:linear-gradient(180deg,#f3e9d8,#e89a4a 55%,#d8b4b0)" role="img" aria-label="Photo of a gelato sandwich with orange and berry scoops"></div>
<span class="category-label" style="left:826px; top:1622px">GELATO</span>
<div class="category-rule" style="left:790px; top:1678px; width:273px"></div>

<div class="abs newsletter-input">Enter email for company news update</div>
<div class="abs newsletter-button">Newsletter</div>
<span class="social-dot" style="left:807px"></span>
<span class="social-dot" style="left:864px"></span>
<span class="social-dot" style="left:922px"></span>
<span class="social-dot" style="left:982px"></span>
<span class="social-dot" style="left:1040px"></span>

<footer class="abs site-footer">
  <div class="footer-col" style="left:117px"><h3>Cakes</h3><ul><li>Mouse Cakes</li><li>Ice cream Cakes</li></ul></div>
  <div class="footer-col" style="left:281px"><h3>Macarons</h3><ul><li>Product 1</li><li>Product 2</li></ul></div>
  <div class="footer-col" style="left:447px"><h3>Cookies</h3><ul><li>Product 1</li><li>Product 2</li></ul></div>
  <div class="footer-col" style="left:612px"><h3>Gelato</h3><ul><li>Sorbet Cream</li></ul></div>
  <div class="footer-col" style="left:777px"><h3>About Us</h3><ul><li>Our Story</li><li>Philosophy</li></ul></div>
  <div class="footer-col" style="left:941px"><h3>Customer Service</h3><ul><li>Contact us</li><li>Shipping</li><li>FAQ</li></ul></div>
  <p class="copyright">© 2015 Lantern&amp;Plum. All rights reserved.</p>
</footer>

</body>
</html>
```